Australia-Wide Industry Leader Bookkeeping Business Website Design Required

We need a website designed for our 10 year old bookkeeping business, Barwick & Lund. Barwick & Lund has been servicing the local & interstate communities of Australia, providing first-class BAS & Bookkeeping services with a personal touch unmatched by anyone else in the county.

What began 10 years ago as a small business focusing on family, friends and the local community, it has since grown into a well respected business with 95% of their business based solely on word of mouth and personal referrals from around Australia.

We would like to see designs that incorporate our existing brand/logo. The colours to be used on the website should be colours that work well with our logo. The design should communicate maturity, trust and confidence with a Web 2.0 look and feel.

We have produced mockups of the entire website as well as assets used in the mockups. Please reference the attached files. The mockups are an example of all the design elements that we want on each page. Designers are encouraged to use the mockups as a guideline only and for designers to use their own creativity.
Updates

This message is for new graphic designers who are considering commencing work on this project. Thank you for expressing an interest in our project. We would like to inform you that this project is close to completion as we have a number designs under very serious consideration.

We are currently in a position where we are disinterested providing feedback to improve on new designs submitted. We will provide feedback to improve new designs only if the submitted designs are very close to what we want for our website, and will only require 1 or 2 revision rounds to refine before the project completion date we will not work with designers to refine their newly submitted designs.

We feel that it is important for all designers to know the above information as we feel that your time and effort may be better spent working on another project.

Thank you for your understanding.

A big thank you for all the designs submitted. We are now in the process of selecting a design. Please be patient during this process. Thank you.

Target Market(s)

Busy Business Owners

Industry/Entity Type

Small Business

Requirements
Must have
• We require a rectangular "slide show" type feature to serve as a "teaser" to arouse the emotions of our website visitors. Each slide asks a specific question. The questions are:

- Is your paperwork in a mess?
- Do you need to get organised for the end of financial year?
- Are you sick & tired of endless amounts of paperwork & BASs?
- Do you feel frustrated & annoyed because you know your books need to be done?
- Do you lack the time & patience to get your paperwork done?
- Do you wish you had more time to do the things you enjoy doing?
- Contact Barwick & Lund today and we will transform your chaos into order.

Underneath the slide show will be a button to "Call Barwick & Lund Now - 03 5550 1827".

```html
<!DOCTYPE html>
<html lang="en">
<head>
<meta charset="utf-8">
<title>Barwick &amp; Lund – BAS &amp; Bookkeeping</title>
<link href="https://fonts.googleapis.com/css2?family=Gelasio:ital,wght@0,400;0,700;1,400;1,700&display=swap" rel="stylesheet">
<style>
:root{
  --wood-dark:#3a2a22;
  --wood-mid:#5a4234;
  --wood-light:#6e5342;
  --pattern:#e4e4e4;
  --paper:#ffffff;
  --red:#a50d10;
  --red-deep:#7e0709;
  --ink:#2b2b2b;
  --grey:#8a8a8a;
  --grey-soft:#b9b9b9;
  --panel:#efefef;
  --green:#2f9a2a;
  --green-deep:#1d7a1b;
  --navy:#0f3f6e;
  --footer:#1f1f1f;
}
*{box-sizing:border-box;margin:0;padding:0}
html,body{width:1097px;height:1200px;overflow:hidden}
body{position:relative;background:var(--wood-mid);font-family:"Gelasio",Georgia,serif;color:var(--ink)}
.wood{position:absolute;left:0;width:1097px;background:linear-gradient(90deg,var(--wood-dark),var(--wood-light) 20%,var(--wood-mid) 45%,var(--wood-light) 70%,var(--wood-dark))}
.wood-top{top:0;height:250px}
.wood-bottom{top:955px;height:200px}
.pattern-band{position:absolute;left:0;top:250px;width:1097px;height:705px;background:var(--pattern)}
.site-footer{position:absolute;left:0;top:1151px;width:1097px;height:49px;background:var(--footer)}

.brand{position:absolute;left:332px;top:0;width:451px;height:91px;background:var(--red);display:flex;align-items:center;justify-content:center;gap:14px}
.brand-mark{width:14px;height:14px;background:var(--paper)}
.brand-name{font-size:44px;color:var(--paper);font-weight:400;letter-spacing:.5px}

.page{position:absolute;left:157px;top:113px;width:783px;height:947px;background:var(--paper)}
.main-nav{height:36px;display:flex;align-items:center;padding:0 14px 0 25px;font-size:15px;color:var(--grey)}
.main-nav a{color:inherit;text-decoration:none;white-space:nowrap;position:relative}
.main-nav a.active{color:var(--red);font-weight:700}
.main-nav a.active::before{content:"";position:absolute;left:-3px;right:-3px;top:-12px;height:4px;background:var(--red)}
.main-nav a.current{color:var(--ink);font-weight:700}
.main-nav .dash{flex:1;height:1px;background:var(--grey-soft);margin:0 4px}

.banner{position:absolute;left:0;top:39px;width:783px;height:94px;background:linear-gradient(180deg,var(--red),var(--red-deep));color:var(--paper);font-style:italic;font-size:15.5px;line-height:23px;text-align:center;padding:12px 30px 0}

.col-main{position:absolute;left:15px;top:162px;width:512px}
h2{font-size:17px;font-weight:400;color:var(--ink);margin-bottom:10px;white-space:nowrap}
h2 em{font-style:normal;color:var(--red)}
.intro p{font-size:10.4px;font-style:italic;color:var(--grey);line-height:15px;margin-bottom:13px}

.ticks{list-style:none;font-size:10.5px;font-style:italic;color:#4a4a4a}
.ticks li{display:flex;align-items:center;gap:8px;height:17.6px}
.tick{width:10px;height:10px;flex:none}
.summary{margin-top:40px}
.summary .ticks{display:grid;grid-template-columns:1fr 1fr;grid-auto-flow:column;grid-template-rows:repeat(6,17.6px)}
.diff{margin-top:30px}
.arrows{list-style:none;margin:8px 0 0 24px;font-size:10px;font-style:italic;font-weight:700;color:#3a3a3a}
.arrows li{display:flex;align-items:center;gap:10px;height:12.5px}
.arrow{width:8px;height:8px;flex:none}
.note{margin:14px 0 0 24px;font-size:10px;font-style:italic;font-weight:700;color:#3a3a3a}
.tagline{position:absolute;left:15px;top:897px;width:512px;font-size:19px;white-space:nowrap;color:var(--grey-soft)}

.col-side{position:absolute;left:551px;top:175px;width:217px}
.teaser{position:relative;height:159px;background:linear-gradient(135deg,#1b5d94,var(--navy) 55%,#0a2c4d)}
.teaser-text{position:absolute;left:12px;top:38px;width:120px;color:var(--paper);font-size:13px;font-weight:700;line-height:17px}
.teaser-dots{position:absolute;left:10px;bottom:10px;display:flex;gap:5px;font-size:8px;color:var(--paper)}
.teaser-dots span{width:10px;text-align:center}
.teaser-dots .on{background:var(--paper);color:var(--navy);border-radius:50%}
.call-now{display:block;height:48px;background:linear-gradient(180deg,#39ad33,var(--green-deep));color:var(--paper);font-size:25px;text-align:center;line-height:48px;text-decoration:none}
.side-box{background:var(--panel);border-top:5px solid var(--red);padding:10px 13px 12px}
.side-box h3{font-size:14px;font-weight:700;color:var(--red);line-height:18px;margin-bottom:8px}
.reach{margin-top:19px;height:277px}
.reach p{font-size:8.5px;font-style:italic;color:#6a6a6a;line-height:11.5px}
.map{margin:14px -13px 0;height:175px;background:linear-gradient(160deg,#d8d8d8,#c4c4c4)}
.quals{margin-top:8px;height:227px}
.quals .ticks{font-size:9.5px}
.quals .ticks li{height:auto;min-height:19px;align-items:flex-start;padding:4px 0;border-bottom:1px solid #dcdcdc;line-height:11px}
.quals .tick{margin-top:1px}

.partners{position:absolute;left:157px;top:1060px;width:783px;height:91px;background:#f3f3f3;display:flex;align-items:center;justify-content:space-around;padding:0 10px}
.badge{background:#cfcfcf}
.follow{position:absolute;left:155px;top:1165px;display:flex;align-items:center;gap:8px;color:var(--paper);font-size:12px;font-style:italic;font-weight:700}
.follow .net{display:flex;align-items:center;gap:4px;font-weight:400;font-size:11px}
.follow .net i{width:12px;height:12px;background:#4f84c4;display:block}
.legal{position:absolute;right:157px;top:1160px;text-align:right;font-size:8.5px;font-style:italic;color:#9a9a9a;line-height:14px}
</style>
</head>
<body>
<svg width="0" height="0" style="position:absolute">
  <defs>
    <symbol id="tick" viewBox="0 0 10 10"><rect width="10" height="10" fill="#2f9a2a"/><path d="M2 5.2 4.2 7.4 8 2.8" fill="none" stroke="#fff" stroke-width="1.6"/></symbol>
    <symbol id="arrow" viewBox="0 0 8 8"><rect width="8" height="8" fill="#a50d10"/><path d="M3 2 5.4 4 3 6" fill="none" stroke="#fff" stroke-width="1.2"/></symbol>
  </defs>
</svg>

<div class="wood wood-top" role="img" aria-label="Dark timber plank background"></div>
<div class="pattern-band" role="img" aria-label="Light grey circle pattern background"></div>
<div class="wood wood-bottom" role="img" aria-label="Dark timber plank background"></div>
<div class="site-footer"></div>

<header class="brand"><span class="brand-mark"></span><span class="brand-name">Barwick &amp; Lund</span></header>

<main class="page">
  <nav class="main-nav">
    <a class="active" href="#">Home</a><span class="dash"></span>
    <a href="#">About Us</a><span class="dash"></span>
    <a href="#">Services</a><span class="dash"></span>
    <a class="current" href="#">Testimonials</a><span class="dash"></span>
    <a href="#">Articles</a><span class="dash"></span>
    <a href="#">Endorsement</a><span class="dash"></span>
    <a href="#">Links</a><span class="dash"></span>
    <a href="#">Contact Us</a>
  </nav>

  <div class="banner">For nearly 10 years Barwick &amp; Lund have been servicing the local &amp; interstate communities of Australia, Providing first-class BAS &amp; Bookkeeping services with a personal touch unmached by anyone els in the country.</div>

  <section class="col-main">
    <div class="intro">
      <h2>Welcome to <em>Barwick &amp; Lund</em></h2>
      <p>Our team keeps the books of busy owners right across the country, so you can spend less time on receipts and more time running the business you built. We handle your BAS, payroll and reconciliations each month, check every figure twice, and explain the results in plain words. From the first meeting we learn how your trade runs, then build a monthly routine that keeps the tax office and your bank manager equally content. Nothing is lodged until you are happy, and you always know who is looking after your accounts.</p>
      <p>Whether you trade from a home office or run a team across several states, we set up simple systems that fit the way you work. Most new clients are surprised how quickly the pile on the desk disappears. Call us for a friendly chat about your paperwork and we will show you where the hours go.</p>
    </div>

    <div class="summary">
      <h2>To <em>Summarise</em></h2>
      <ul class="ticks">
        <li><svg class="tick"><use href="#tick"/></svg>FREE initial consultation</li>
        <li><svg class="tick"><use href="#tick"/></svg>Registerd BAS Agent - 91482-003</li>
        <li><svg class="tick"><use href="#tick"/></svg>Bookkeeping</li>
        <li><svg class="tick"><use href="#tick"/></svg>BAS Preparation &amp; Lodgement</li>
        <li><svg class="tick"><use href="#tick"/></svg>Payroll</li>
        <li><svg class="tick"><use href="#tick"/></svg>IAS Preparation &amp; Lodgement</li>
        <li><svg class="tick"><use href="#tick"/></svg>Superannuation &amp; Workcover</li>
        <li><svg class="tick"><use href="#tick"/></svg>Margin Schem</li>
        <li><svg class="tick"><use href="#tick"/></svg>Fule Tax Credits</li>
        <li><svg class="tick"><use href="#tick"/></svg>Offsite &amp; Onsite Bookkeeping</li>
        <li><svg class="tick"><use href="#tick"/></svg>Tallybook Software &amp; Training</li>
        <li><svg class="tick"><use href="#tick"/></svg>Australia Wide</li>
      </ul>
    </div>

    <div class="diff">
      <h2>What <em>makers Barwick &amp; Lund Different from other Bookkeepers</em></h2>
      <ul class="ticks">
        <li><svg class="tick"><use href="#tick"/></svg>We guarantee the quality of our work</li>
        <li><svg class="tick"><use href="#tick"/></svg>We have over 35 years of experience</li>
        <li><svg class="tick"><use href="#tick"/></svg>We have owned &amp; operated businesses for 35 years</li>
        <li><svg class="tick"><use href="#tick"/></svg>The Barwick &amp; Lund team are investor &amp; traders</li>
        <li><svg class="tick"><use href="#tick"/></svg>Extensive business network for your benefit</li>
        <li><svg class="tick"><use href="#tick"/></svg>Backed by a team of Accountants</li>
        <li><svg class="tick"><use href="#tick"/></svg>Wework a team of elite accounts &amp; wealth creation professionals who coach us monthly in the following:</li>
      </ul>
      <ul class="arrows">
        <li><svg class="arrow"><use href="#arrow"/></svg>Asset Protecion</li>
        <li><svg class="arrow"><use href="#arrow"/></svg>Superannuation &amp; Self Managed Superannuation Funds</li>
        <li><svg class="arrow"><use href="#arrow"/></svg>Property Investing</li>
        <li><svg class="arrow"><use href="#arrow"/></svg>Tax Strategies, tax starcteres &amp; best tax Saving</li>
      </ul>
      <p class="note">We understand just how important it is to help lead &amp; guide our clients from making profits to:</p>
      <ul class="arrows">
        <li><svg class="arrow"><use href="#arrow"/></svg>Maximising profits</li>
        <li><svg class="arrow"><use href="#arrow"/></svg>Welth creation</li>
        <li><svg class="arrow"><use href="#arrow"/></svg>Tax minimisation</li>
        <li><svg class="arrow"><use href="#arrow"/></svg>Asset protection</li>
      </ul>
    </div>
  </section>
  <p class="tagline">This is something that other bookkeeping just don't do!</p>

  <aside class="col-side">
    <div class="teaser" role="img" aria-label="Slideshow photo of a raised hand over a pile of paperwork">
      <p class="teaser-text">Are you sick &amp; tired of endless amounts of paperwork &amp; BASs?</p>
      <div class="teaser-dots"><span class="on">1</span><span>2</span><span>3</span><span>4</span><span>5</span><span>6</span></div>
    </div>
    <a class="call-now" href="#">Call Us Now</a>

    <section class="side-box reach">
      <h3>Servicing all of Australia</h3>
      <p>95% of our clients come from client &amp; accountant referrals. We have clients all over Victoria, Queensland, NSW &amp; Western Australia, so no matter you are, we can help</p>
      <div class="map" role="img" aria-label="Map of Australia with client locations marked"></div>
    </section>

    <section class="side-box quals">
      <h3>Qualification, Members and Partnership</h3>
      <ul class="ticks">
        <li><svg class="tick"><use href="#tick"/></svg>Registerd Tax Office BAS Agent</li>
        <li><svg class="tick"><use href="#tick"/></svg>Certificate IV Financial Services</li>
        <li><svg class="tick"><use href="#tick"/></svg>Certificate III Financial Services</li>
        <li><svg class="tick"><use href="#tick"/></svg>Member of Guild of Chartered Bookkeepers</li>
        <li><svg class="tick"><use href="#tick"/></svg>Platinum Member of Ledger Circle</li>
        <li><svg class="tick"><use href="#tick"/></svg>Ledgerly Professional Partner</li>
        <li><svg class="tick"><use href="#tick"/></svg>Tax Wise Network</li>
      </ul>
    </section>
  </aside>
</main>

<div class="partners">
  <div class="badge" style="width:34px;height:56px"></div>
  <div class="badge" style="width:56px;height:50px"></div>
  <div class="badge" style="width:52px;height:56px"></div>
  <div class="badge" style="width:190px;height:40px"></div>
  <div class="badge" style="width:30px;height:56px"></div>
</div>

<div class="follow">Follow us
  <span class="net"><i></i>Friendnet</span>
  <span class="net"><i></i>Chirpline</span>
</div>
<p class="legal">The contents of this site are copyright © 2011. Barwick &amp; Lund. All Rights Reserved.<br>This page was last modified Sat 25 June 2011</p>
</body>
</html>
```